Webdesign für ein Dachdeckerbetrieb
Zielgruppe
Wir sind ein Dachdeckerbetrieb.
Zielgruppe sind öffentliche Auftrageber , Hausverwaltungen und private Hausbesitzer.
Aufgabenstellung
Die Seite sollte übersichtlich sein. Nicht zuviele Menüs durch die man klicken muss.
Bilder können wir liefern .
Nach Vorgabe des Designers beschaffen wir die Bilder .
Logo ist vorhanden.

```html
<!DOCTYPE html>
<html lang="de">
<head>
<meta charset="utf-8">
<title>Hallwig Dachbau – Dachdecker und Zimmerer</title>
<link rel="stylesheet" href="https://fonts.googleapis.com/css2?family=Source+Sans+3:wght@400;600;700&display=swap">
<style>
  :root {
    --green: #93ad22;
    --green-dark: #86a01c;
    --hero-dark: #4e4e50;
    --footer: #474747;
    --text: #333333;
    --muted: #6f6f6f;
    --caption-bg: #e9ebd5;
    --white: #ffffff;
  }
  * { margin: 0; padding: 0; box-sizing: border-box; }
  html, body { width: 1200px; height: 3111px; overflow: hidden; }
  body {
    position: relative;
    background: var(--white);
    font-family: "Source Sans 3", "Source Sans Pro", Arial, sans-serif;
    color: var(--text);
  }
  .abs { position: absolute; }
  a { color: inherit; text-decoration: none; }

  /* Header */
  .brand { left: 193px; top: 34px; display: flex; align-items: center; gap: 6px; white-space: nowrap; }
  .brand-mark { width: 11px; height: 11px; background: var(--green); }
  .brand-name { color: var(--green); font-weight: 700; font-size: 15px; line-height: 18px; }
  .header-phone { left: 331px; top: 36px; font-size: 12px; color: var(--muted); white-space: nowrap; }
  .main-nav { top: 36px; font-size: 12px; font-weight: 600; color: var(--text); }
  .btn-outline {
    left: 940px; top: 32px; width: 66px; height: 26px;
    border: 1px solid var(--green); border-radius: 13px;
    color: var(--green); font-size: 11px; font-weight: 600;
    display: flex; align-items: center; justify-content: center;
  }

  /* Hero */
  .hero-panel { left: 0; top: 82px; width: 599px; height: 439px; background: var(--hero-dark); }
  .hero-photo { left: 599px; top: 82px; width: 601px; height: 439px;
    background: linear-gradient(135deg, #8fa3bb 0%, #c7cdd3 35%, #b19386 60%, #6f5a50 100%); }
  .hero-rule { left: 0; top: 521px; width: 1200px; height: 6px; background: var(--green); }
  .hero-title { left: 193px; top: 186px; width: 320px; color: var(--white);
    font-size: 25px; font-weight: 700; line-height: 28px; }
  .hero-text { left: 193px; top: 287px; width: 262px; color: #e6e6e6;
    font-size: 12px; line-height: 16px; }

  .btn {
    position: absolute; height: 33px; border-radius: 17px; background: var(--green);
    color: var(--white); font-size: 12px; font-weight: 600;
    display: flex; align-items: center; justify-content: center;
  }

  /* Content */
  .intro { left: 263px; top: 606px; width: 680px; font-size: 18px; line-height: 25px; color: var(--text); }
  .photo { position: absolute; }
  .feature-title { position: absolute; color: var(--green); font-size: 24px; font-weight: 700; line-height: 28px; width: 300px; }
  .feature-text { position: absolute; font-size: 11px; line-height: 15.7px; color: var(--text); width: 260px; }

  .service-tick { left: 275px; top: 1103px; }
  .service-list { left: 339px; top: 1133px; width: 540px; font-size: 17px; line-height: 25px; color: var(--muted); }

  /* References */
  .section-title { left: 0; width: 1200px; text-align: center; font-size: 18px; font-weight: 700; color: #444; }
  .ref-card { position: absolute; width: 193px; height: 145px; border-radius: 4px; overflow: hidden;
    background: var(--caption-bg); box-shadow: 0 1px 3px rgba(0,0,0,.12); }
  .ref-image { width: 100%; height: 115px; }
  .ref-caption { padding: 7px 14px 0; font-size: 9.5px; color: #555; }
  .show-all { left: 562px; top: 2364px; width: 70px; text-align: center; font-size: 11px; color: #555;
    border-bottom: 1px solid #555; padding-bottom: 2px; }

  .claim { left: 332px; top: 2458px; width: 600px; font-size: 19.5px; line-height: 30px; color: var(--text); }

  .partner-badge { position: absolute; top: 2728px; height: 24px; border-radius: 5px; background: #3b3f4a; }

  /* Footer */
  .site-footer { left: 0; top: 2831px; width: 1200px; height: 280px; background: var(--footer); color: #e8e8e8; }
  .footer-address { left: 258px; top: 75px; font-size: 11px; line-height: 16px; }
  .footer-address strong { font-weight: 700; }
  .footer-contact { left: 258px; top: 130px; font-size: 11px; line-height: 18px; }
  .footer-contact a { text-decoration: underline; display: block; }
  .footer-nav { left: 602px; top: 72px; font-size: 12px; font-weight: 600; line-height: 23.5px; }
  .footer-legal { top: 244px; font-size: 9px; color: #bbbbbb; }
</style>
</head>
<body>

<header>
  <div class="abs brand"><span class="brand-mark"></span><span class="brand-name">Hallwig Dachbau</span></div>
  <div class="abs header-phone">06541 - 72 40 18</div>
  <nav>
    <a class="abs main-nav" style="left:605px" href="#">Leistungen</a>
    <a class="abs main-nav" style="left:699px" href="#">Über uns</a>
    <a class="abs main-nav" style="left:785px" href="#">Referenzen</a>
  </nav>
  <a class="abs btn-outline" href="#">Anfrage</a>
</header>

<section class="hero">
  <div class="abs hero-panel"></div>
  <div class="abs hero-photo" role="img" aria-label="Dachdecker bei der Arbeit auf einem Schrägdach"></div>
  <div class="abs hero-rule"></div>
  <h1 class="abs hero-title">Starke und zuverlässige Dachdecker und&nbsp; Zimmerer für Ihre Dachsanierung</h1>
  <p class="abs hero-text">Als Dachdecker-Meisterbetrieb sind wir der richtige Ansprechpartner für alle Arbeiten rund um ein fachgerechtes Dach, sowohl im privaten als auch im gewerblichen Bereich.</p>
  <a class="btn" style="left:188px;top:386px;width:148px" href="#">Angebot einholen</a>
</section>

<p class="abs intro">Wir helfen Ihnen persönliche Wünsche mit technisch und fachlich richtigen Lösungen umzusetzen. Egal, ob Sie eine Neueindeckung oder eine Sanierung Ihres Wohnhauses wünschen, eine Wärmedämmung nach den neuesten gesetzlichen Vorgaben umgesetzt oder ein Dachfenster eingebaut werden soll.</p>

<div class="photo" style="left:193px;top:751px;width:401px;height:265px;background:linear-gradient(135deg,#3c4a5c 0%,#5a6472 45%,#c9a77c 80%,#e1c49a 100%)" role="img" aria-label="Dachdecker auf dem Gerüst beim Eindecken eines Ziegeldachs"></div>
<h2 class="feature-title" style="left:675px;top:829px">Für ein&nbsp; sicheres und langlebiges Zuhause</h2>
<p class="feature-text" style="left:675px;top:905px;width:272px">Unsere erfahrene&nbsp; Dachdecker und Zimmerer bauen Ihnen ein qualitativ hochwertiges Dach, das Sie bei „Wind und Wetter“ schützt und Ihnen ein sicheres und langlebiges Zuhause bietet.</p>
<a class="btn" style="left:672px;top:984px;width:146px" href="#">Unsere Leistungen</a>

<svg class="abs service-tick" width="48" height="48" viewBox="0 0 48 48" aria-hidden="true">
  <circle cx="24" cy="24" r="24" fill="var(--green)"/>
  <path d="M14 24.5 L21 31 L34 17" fill="none" stroke="#fff" stroke-width="3" stroke-linecap="round" stroke-linejoin="round"/>
</svg>
<p class="abs service-list">Ziegeldach | Flachdach | Abdichtungstechnik | Reparaturen &amp; Wartung | Bauklempnerei | Stehfalzarbeiten | Dacherneuerungen | Dachumbauten | Einbau von Dachflächenfenstern</p>

<h2 class="feature-title" style="left:262px;top:1315px">Aus Überzeugung und Freude am Tun</h2>
<p class="feature-text" style="left:262px;top:1390px">Der Herausforderung ein Steildach, Ziegeldach oder Flachdach fachmännisch zu decken, stellen wir uns täglich gerne. Wir nehmen Ihre Wünsche in unserer anschließenden Planung auf und erarbeiten mit Ihnen und für Sie die optimale Lösung.</p>
<a class="btn" style="left:262px;top:1485px;width:134px" href="#">Mehr über uns</a>
<div class="photo" style="left:614px;top:1272px;width:390px;height:260px;background:linear-gradient(180deg,#6f8fb5 0%,#b9c8d8 45%,#5f6b73 75%,#2c3a52 100%)" role="img" aria-label="Dachdecker auf einem Dach mit Solarmodulen im Hintergrund"></div>

<div class="photo" style="left:193px;top:1620px;width:401px;height:270px;background:linear-gradient(180deg,#a9b6a3 0%,#7d8e5a 35%,#b39a74 65%,#d9d9d6 100%)" role="img" aria-label="Dachlattung mit Hammer auf einer Betonkante"></div>
<h2 class="feature-title" style="left:675px;top:1660px">Fachbetrieb und zuverlässiger Partner</h2>
<p class="feature-text" style="left:675px;top:1736px;width:250px">Unser Fachbetrieb ist Ihr zuverlässiger und fachkundiger Partner in allen Fragen rund um das Thema Bedachungen. Wir unterstützen Sie bei der Planung und Durchführung von sämtlichen Dachdeckerarbeiten.</p>
<a class="btn" style="left:675px;top:1829px;width:147px" href="#">Unsere Referenzen</a>

<h2 class="abs section-title" style="top:1998px">Referenzen</h2>

<div class="ref-card" style="left:192px;top:2045px"><div class="ref-image" style="background:linear-gradient(180deg,#8fb3cf,#5c6a74 60%,#8a4a3c)" role="img" aria-label="Historisches Gebäude mit Schieferdach"></div><div class="ref-caption">Bauvorhaben Mainz</div></div>
<div class="ref-card" style="left:401px;top:2045px"><div class="ref-image" style="background:linear-gradient(135deg,#c29a4e,#8c6a30 55%,#2f5a8c)" role="img" aria-label="Firmengebäude mit Metallfassade"></div><div class="ref-caption">Firmengebäude Darmstadt</div></div>
<div class="ref-card" style="left:610px;top:2045px"><div class="ref-image" style="background:linear-gradient(180deg,#d9dde0,#6d7276 50%,#8a8f93)" role="img" aria-label="Mehrfamilienhaus mit Stehfalzdach"></div><div class="ref-caption">Mehrfamilienhaus Frankfurt</div></div>
<div class="ref-card" style="left:816px;top:2045px"><div class="ref-image" style="background:linear-gradient(180deg,#e3e6ea,#b8b4ad 55%,#8e7b66)" role="img" aria-label="Einfamilienhaus mit hellem Dach"></div><div class="ref-caption">Einfamilienhaus Frankfurt</div></div>
<div class="ref-card" style="left:192px;top:2199px"><div class="ref-image" style="background:linear-gradient(180deg,#7f9ec0,#d8d6cf 55%,#6b5b4a)" role="img" aria-label="Verwaltungsgebäude mit Walmdach"></div><div class="ref-caption">Verwaltungsgebäude Hanau</div></div>
<div class="ref-card" style="left:401px;top:2199px"><div class="ref-image" style="background:linear-gradient(180deg,#d9e3ea,#b8553d 35%,#e8e6e0 60%,#7d7a6e)" role="img" aria-label="Gutshof mit Ziegeldach"></div><div class="ref-caption">Gutshof Kranichstein</div></div>
<div class="ref-card" style="left:610px;top:2199px"><div class="ref-image" style="background:linear-gradient(135deg,#c8502f,#a53b22 55%,#2f6b6a)" role="img" aria-label="Mehrfamilienhaus mit roten Dachziegeln und Gauben"></div><div class="ref-caption">Mehrfamilienhaus Bingen</div></div>
<div class="ref-card" style="left:816px;top:2199px"><div class="ref-image" style="background:linear-gradient(160deg,#2f3035,#44464c 50%,#c95a4a 80%,#d9dde2)" role="img" aria-label="Firmengebäude mit dunklem Flachdach"></div><div class="ref-caption">Firmengebäude Frankfurt</div></div>

<a class="abs show-all" href="#">Alle anzeigen</a>

<p class="abs claim">Solides Handwerk und Können ist eine Sache, Vertrauen eine andere. Wir sind Ihr Partner für ausdrucksstarke und sichere Dächer.</p>
<a class="btn" style="left:327px;top:2538px;width:149px" href="#">Angebot einholen</a>

<h2 class="abs section-title" style="top:2680px">Unsere Partner</h2>
<div class="partner-badge" style="left:266px;width:86px" aria-label="Partner"></div>
<div class="partner-badge" style="left:453px;width:106px" aria-label="Partner"></div>
<div class="partner-badge" style="left:661px;width:84px" aria-label="Partner"></div>
<div class="partner-badge" style="left:840px;width:97px" aria-label="Partner"></div>

<footer class="abs site-footer">
  <div class="abs footer-address"><strong>Hallwig Dachbau</strong><br>Lindenweg 12<br>55270 Obertal</div>
  <div class="abs footer-contact"><a href="#">info@hallwig-dachbau.de</a><a href="#">06541 - 72 40 18</a></div>
  <nav class="abs footer-nav"><a href="#" style="display:block">Leistungen</a><a href="#" style="display:block">Über uns</a><a href="#" style="display:block">Referenzen</a><a href="#" style="display:block">Anfrage</a></nav>
  <a class="abs footer-legal" style="left:258px" href="#">Impressum</a>
  <a class="abs footer-legal" style="left:326px" href="#">Datenschutz</a>
</footer>

</body>
</html>
```